Letterhead creation for military law attorney

I need letterhead design for my business. We are now only doing military law and need to change address, logo and vision. I like the idea of using an eagle or a jolly roger flag

Target Market(s)

Military Law Clients

Colors
3176b5
85abd2

Requirements
Must have
• We are defending people against the government
Nice to have
• Jolly Roger Flag

```html
<!DOCTYPE html>
<html lang="en">
<head>
<meta charset="utf-8">
<title>Brandt Defense Group — Letterhead</title>
<link rel="stylesheet" href="https://fonts.googleapis.com/css2?family=Open+Sans:ital,wght@0,300;0,400;0,600;1,300&family=Roboto+Condensed:wght@700&display=swap">
<style>
  :root {
    --backdrop: #6fa3a5;
    --paper: #ffffff;
    --ink: #111111;
    --body-grey: #6b6b6b;
    --rule: #1a1a1a;
    --footer-text: #ffffff;
  }
  html, body {
    margin: 0;
    width: 1200px;
    height: 900px;
    overflow: hidden;
    background: var(--backdrop);
  }
  .letterhead {
    position: absolute;
    left: 300px;
    top: 22px;
    width: 600px;
    height: 856px;
    background: var(--paper);
    box-shadow: 0 10px 30px rgba(0,0,0,0.25);
    overflow: hidden;
    font-family: "Open Sans", sans-serif;
  }
  .header-rules {
    position: absolute;
    left: 0;
    top: 0;
    width: 600px;
    height: 160px;
  }
  .brand {
    position: absolute;
    right: 44px;
    top: 60px;
    display: flex;
    align-items: center;
    gap: 10px;
  }
  .brand-mark {
    width: 12px;
    height: 12px;
    background: var(--ink);
  }
  .brand-name {
    font-family: "Open Sans", sans-serif;
    font-weight: 600;
    font-size: 16px;
    letter-spacing: 0;
    color: var(--ink);
  }
  .letter {
    position: absolute;
    left: 56px;
    top: 168px;
    width: 470px;
    color: var(--body-grey);
    font-weight: 300;
    font-size: 10.5px;
    line-height: 18px;
  }
  .letter-date { margin: 0 0 14px; font-style: italic; }
  .letter p { margin: 0 0 10px; }
  .sign-off {
    position: absolute;
    left: 340px;
    top: 600px;
    color: var(--body-grey);
    font-size: 11px;
    line-height: 15px;
  }
  .signature {
    width: 120px;
    height: 34px;
    margin-bottom: 4px;
    background: linear-gradient(90deg, rgba(185,185,185,0.15), rgba(185,185,185,0.45), rgba(185,185,185,0.15));
    border-radius: 3px;
  }
  .signer-name { display: block; color: #444; }
  .footer-band {
    position: absolute;
    left: 0;
    bottom: 0;
    width: 600px;
    height: 62px;
    background: var(--ink);
    display: flex;
    align-items: center;
    padding-left: 40px;
    box-sizing: border-box;
  }
  .footer-contact {
    margin: 0;
    font-family: "Roboto Condensed", sans-serif;
    font-weight: 700;
    font-size: 12px;
    color: var(--footer-text);
    letter-spacing: 0.3px;
  }
  .footer-contact .divider { margin: 0 8px; opacity: 0.8; }
  .footer-mark {
    position: absolute;
    right: 34px;
    bottom: 20px;
    width: 22px;
    height: 22px;
    border-radius: 50%;
    background: var(--footer-text);
  }
</style>
</head>
<body>
  <main class="letterhead">
    <svg class="header-rules" viewBox="0 0 600 160" aria-hidden="true">
      <line x1="150" y1="50" x2="430" y2="50" stroke="var(--rule)" stroke-width="1.2"/>
      <path d="M 240 110 Q 420 150 570 135" fill="none" stroke="var(--rule)" stroke-width="1.4"/>
      <path d="M 0 0 L 600 0 L 600 6 Q 300 -2 0 6 Z" fill="var(--ink)"/>
    </svg>

    <div class="brand">
      <span class="brand-mark"></span>
      <span class="brand-name">Brandt Defense Group</span>
    </div>

    <article class="letter">
      <p class="letter-date">Date, 10 September, 2020</p>
      <p>This is a sample letter that has been placed to demonstrate typing format (Your Company) letterhead design. When positioned properly, it will serve to work in harmony with all other elements letterhead. This letterhead design is meant to project an image.</p>
      <p>This letterhead design is meant to project an image of professionalism and reliability. By using simple alignment we have created a very spacious feeling. The simplicity suggests strength, the spaciousness contributes to aesthetics and the layout. These basic qualities along with the (Your Company) look and help reinforce the (Your Company) brand. This letterhead design is meant to project an image of design. When positioned properly, it will serve to work in harmony with all the other elements of the letterhead, professionalism and reliability.</p>
      <p>This letterhead design is based on the (Form of your logo) form (Your Company) logo. Each stationery piece we have created has a very spacious feeling. The simplicity suggests strength, the spaciousness contributes part of the (Form of your logo).</p>
    </article>

    <div class="sign-off">
      <div class="signature" role="img" aria-label="Handwritten signature of Daniel Reeve"></div>
      <span class="signer-name">Daniel Reeve</span>
      <span class="signer-role">Manager</span>
    </div>

    <footer class="footer-band">
      <p class="footer-contact">
        P: (555) 014-2270<span class="divider">|</span>F: (555) 014-2271<span class="divider">|</span>PO Box 320 Fairview, TN 37000
      </p>
      <span class="footer-mark"></span>
    </footer>
  </main>
</body>
</html>
```